Have Logo - Need Business Card Design!!!

I am looking for a business card design for a real estate development business. The company name is Harlow Crest Properties. I already have a logo created by Artisan Hive and would like this logo to be incorporated into the design. I have uploaded the files. The card needs to be professional, but visually interesting. Not necessary to be double-sided, but if you want to get creative and can think of something to put on the back then have at it.

Target Market(s)

The target audience for these business cards will be professionals in the real estate industry.

Industry/Entity Type

Real Estate

Requirements
Must have
• The business card must have all the necessary items for a business card, i.e. company name, our logo, name (however, not title necessary), office address, office phone number, cell number, fax number, website address, etc.

You can use the information below for the card:

Gregory L. Danforth
718 Ridgemont Avenue
San Francisco, California 94382

www.harlowcrest.example
gdanforth@harlowcrest.example
Office: 415-555-0143
Fax: 415-555-0147
Cell: 415-555-0186

```html
<!DOCTYPE html>
<html lang="en">
<head>
<meta charset="utf-8">
<title>Harlow Crest Properties – Business Card</title>
<link href="https://fonts.googleapis.com/css2?family=Open+Sans:wght@400;600;700&display=swap" rel="stylesheet">
<style>
  :root {
    --backdrop: #e4e8e8;
    --card-white: #ffffff;
    --brand-blue: #0a2394;
    --label-green: #3fd13f;
    --text-white: #ffffff;
  }
  * { margin: 0; padding: 0; box-sizing: border-box; }
  html, body {
    width: 1200px; height: 1015px; overflow: hidden;
    background: var(--backdrop);
    font-family: "Open Sans", Arial, sans-serif;
  }
  .canvas { position: relative; width: 1200px; height: 1015px; }

  .card { position: absolute; left: 353px; width: 495px; background: var(--card-white); }
  .card--front { top: 162px; height: 311px; display: flex; align-items: center; justify-content: center; }
  .card--back { top: 545px; height: 309px; }

  .wordmark {
    color: var(--brand-blue); font-weight: 600; white-space: nowrap; letter-spacing: 0.3px;
  }
  .card--front .wordmark { font-size: 28px; line-height: 40px; }

  .card__strip { position: absolute; left: 0; top: 0; width: 116px; height: 100%; background: var(--card-white); }
  .card--back .wordmark {
    position: absolute; left: 57px; top: 155px;
    font-size: 19px; line-height: 26px;
    transform: translate(-50%, -50%) rotate(-90deg);
  }

  .card__panel { position: absolute; left: 116px; top: 0; right: 0; height: 100%; background: var(--brand-blue); }

  .contact { position: absolute; left: 143px; top: 106px; color: var(--text-white); }
  .contact__name { font-size: 14.5px; font-weight: 600; letter-spacing: 0.2px; line-height: 18px; }
  .contact__title { font-size: 12.5px; font-weight: 600; line-height: 17px; }
  .contact__list { margin-top: 14px; }
  .contact__row { position: relative; font-size: 13px; line-height: 19.5px; }
  .contact__label {
    position: absolute; right: 100%; width: 80px; margin-right: 7px;
    text-align: right; color: var(--label-green); text-transform: uppercase;
  }
  .contact__value { display: block; white-space: nowrap; }
  .contact__value--address { line-height: 15px; padding-top: 2px; }
</style>
</head>
<body>
<main class="canvas">
  <section class="card card--front" aria-label="Card front">
    <div class="wordmark">Harlow Crest Properties</div>
  </section>

  <section class="card card--back" aria-label="Card back">
    <div class="card__strip">
      <div class="wordmark">Harlow Crest Properties</div>
    </div>
    <div class="card__panel">
      <div class="contact">
        <p class="contact__name">GREGORY L. DANFORTH</p>
        <p class="contact__title">REALTOR</p>
        <div class="contact__list">
          <p class="contact__row"><span class="contact__label">Cell</span><span class="contact__value">415-555-0186</span></p>
          <p class="contact__row"><span class="contact__label">Office</span><span class="contact__value">415-555-0143</span></p>
          <p class="contact__row"><span class="contact__label">Fax</span><span class="contact__value">415-555-0147</span></p>
          <p class="contact__row"><span class="contact__label">Email</span><span class="contact__value">gdanforth@harlowcrest.example</span></p>
          <p class="contact__row"><span class="contact__label">Website</span><span class="contact__value">www.harlowcrest.example</span></p>
          <p class="contact__row"><span class="contact__label">Address</span><span class="contact__value contact__value--address">718 Ridgemont Avenue<br>San Francisco, California 94382</span></p>
        </div>
      </div>
    </div>
  </section>
</main>
</body>
</html>
```